Veltrano - Mechanic/Collision Center Business Card

We're looking for a business card design for our mechanic/ collision repair shop.

Can be with colours or monochromatic.

See the attached files.

Many thanks

```html
<!DOCTYPE html>
<html lang="pt">
<head>
<meta charset="utf-8">
<title>Veltrano – Business Card</title>
<link href="https://fonts.googleapis.com/css2?family=Open+Sans:wght@400;600;800&display=swap" rel="stylesheet">
<style>
  :root {
    --canvas-bg: #e4e4e2;
    --card-blue: #13709a;
    --card-white: #f7f7f7;
    --ink-dark: #1c2124;
    --accent-blue: #1e8fd5;
    --text-grey: #6e6e6e;
    --text-black: #1a1a1a;
    --divider: #c9c9c9;
  }
  * { box-sizing: border-box; margin: 0; padding: 0; }
  html, body { width: 1200px; height: 900px; overflow: hidden; }
  body {
    background: var(--canvas-bg);
    font-family: "Open Sans", Arial, sans-serif;
    display: flex;
    flex-direction: column;
    align-items: center;
    justify-content: center;
    gap: 40px;
  }
  .card {
    width: 620px;
    height: 376px;
    position: relative;
    box-shadow: 0 6px 18px rgba(0,0,0,0.18);
  }
  .card-front {
    background: var(--card-blue);
    display: flex;
    align-items: center;
    justify-content: center;
  }
  .front-brand {
    color: var(--ink-dark);
    font-weight: 800;
    font-size: 78px;
    letter-spacing: 2px;
    text-transform: uppercase;
  }
  .card-back { background: var(--card-white); }
  .back-header {
    position: absolute;
    top: 34px;
    left: 34px;
    display: flex;
    align-items: center;
  }
  .back-brand {
    color: var(--accent-blue);
    font-weight: 800;
    font-size: 26px;
    text-transform: uppercase;
    letter-spacing: 1px;
    padding-right: 14px;
  }
  .header-divider {
    width: 1px;
    height: 58px;
    background: var(--divider);
    margin-right: 14px;
  }
  .person-name {
    color: var(--accent-blue);
    font-weight: 600;
    font-size: 34px;
    line-height: 1.05;
  }
  .person-role {
    color: var(--text-grey);
    font-weight: 600;
    font-size: 21px;
    line-height: 1.1;
  }
  .contact-block {
    position: absolute;
    right: 34px;
    bottom: 28px;
    text-align: right;
  }
  .contact-list { list-style: none; }
  .contact-item {
    display: flex;
    justify-content: flex-end;
    align-items: center;
    gap: 10px;
    font-size: 13px;
    color: var(--text-black);
    line-height: 24px;
  }
  .contact-icon { width: 16px; height: 16px; flex: none; }
  .contact-address {
    margin-top: 6px;
    font-weight: 600;
    font-size: 18px;
    line-height: 1.3;
    color: var(--text-black);
    padding-right: 26px;
  }
</style>
</head>
<body>

  <section class="card card-front">
    <span class="front-brand">Veltrano</span>
  </section>

  <section class="card card-back">
    <header class="back-header">
      <span class="back-brand">Veltrano</span>
      <span class="header-divider"></span>
      <div class="person">
        <div class="person-name">Tiago Moreira</div>
        <div class="person-role">Manager</div>
      </div>
    </header>

    <div class="contact-block">
      <ul class="contact-list">
        <li class="contact-item">veltrano.oficina@mail.pt
          <svg class="contact-icon" viewBox="0 0 16 16" fill="none" stroke="#1e8fd5" stroke-width="1.2"><rect x="1.5" y="3.5" width="13" height="9"/><path d="M1.5 3.5 8 9l6.5-5.5"/></svg>
        </li>
        <li class="contact-item">+351 214550382
          <svg class="contact-icon" viewBox="0 0 16 16" fill="none" stroke="#1e8fd5" stroke-width="1.2"><path d="M3 2c-1 1-1.5 2.5 0 5s4 5.5 6.5 7c1.5.8 2.5.5 3.5-.5l-2.3-2.3-1.7 1c-1.5-.8-3.4-2.8-4.2-4.3l1-1.7L3.5 1.8z"/></svg>
        </li>
        <li class="contact-item">+351 936204718
          <svg class="contact-icon" viewBox="0 0 16 16" fill="none" stroke="#1e8fd5" stroke-width="1.2"><rect x="4" y="1" width="8" height="14" rx="1"/><path d="M7 12.8h2"/></svg>
        </li>
        <li class="contact-item">www.veltrano-oficina.pt
          <svg class="contact-icon" viewBox="0 0 16 16" fill="none" stroke="#1e8fd5" stroke-width="1.2"><circle cx="8" cy="8" r="6.5"/></svg>
        </li>
      </ul>
      <address class="contact-address" style="font-style: normal;">
        Rua das Oliveiras 42<br>2700-118 Amadora
      </address>
    </div>
  </section>

</body>
</html>
```